Looking for a Lumora Book Cover

My book has been online for a while and I am now looking for a professional cover for it as it has been very well received.

You can view the book here and all the details about it:

https://www.pagevaultshop.example/dp/X7Q2KRMTPL#readerNotes

Not sure what I am looking for as a design, just open to your ideas.

I want something different that will stand out please.

Thanks
Owen

```html
<!DOCTYPE html>
<html lang="en">
<head>
<meta charset="utf-8">
<title>Roots &amp; Resilience — Book Cover</title>
<link rel="stylesheet" href="https://fonts.googleapis.com/css2?family=Anton&family=Archivo:wght@700;800&family=Arimo:ital,wght@0,400;1,400&display=swap">
<style>
  :root {
    --ink: #000000;
    --paper: #ffffff;
    --accent-red: #c40000;
    --ampersand-grey: #555555;
  }
  html, body {
    margin: 0;
    padding: 0;
    width: 800px;
    height: 1200px;
    overflow: hidden;
    background: var(--ink);
  }
  .cover {
    position: relative;
    width: 800px;
    height: 1200px;
    background: var(--ink);
    overflow: hidden;
  }
  .cover-art {
    position: absolute;
    inset: 0;
  }
  .title-block {
    position: absolute;
    left: 0;
    top: 0;
  }
  .title-word {
    font-family: "Anton", "Impact", sans-serif;
  }
  .subtitle-band {
    position: absolute;
    left: 60px;
    top: 766px;
    width: 549px;
    height: 90px;
    margin: 0;
    background: var(--accent-red);
    box-sizing: border-box;
    padding: 3px 10px 0 0;
    text-align: right;
    color: var(--paper);
    font-family: "Archivo", "Helvetica Neue", Arial, sans-serif;
    font-weight: 700;
    font-size: 37px;
    line-height: 42px;
    letter-spacing: 0.2px;
  }
  .tagline {
    position: absolute;
    left: 0;
    width: 800px;
    top: 1020px;
    margin: 0;
    text-align: center;
    color: var(--paper);
    font-family: "Arimo", "Helvetica Neue", Arial, sans-serif;
    font-size: 26px;
    line-height: 28px;
  }
  .tagline em {
    color: var(--accent-red);
  }
  .author {
    position: absolute;
    left: 0;
    width: 800px;
    top: 1108px;
    margin: 0;
    text-align: center;
    color: var(--paper);
    font-family: "Archivo", "Helvetica Neue", Arial, sans-serif;
    font-weight: 800;
    font-size: 34px;
    letter-spacing: -0.5px;
    line-height: 40px;
  }
</style>
</head>
<body>
  <main class="cover">
    <svg class="cover-art" width="800" height="1200" viewBox="0 0 800 1200">
      <defs>
        <linearGradient id="portraitTone" x1="0" y1="0" x2="1" y2="0">
          <stop offset="0" stop-color="#000000"/>
          <stop offset="0.5" stop-color="#1c0808"/>
          <stop offset="0.78" stop-color="#6a0000"/>
          <stop offset="1" stop-color="#c40000"/>
        </linearGradient>
      </defs>
      <path role="img" aria-label="Textured photographic profile portrait of a Black woman gazing upward, set against a red backdrop"
            d="M460 0 H800 V1070 C730 1040 640 1010 590 990 C520 700 480 300 460 0 Z"
            fill="url(#portraitTone)"/>
    </svg>

    <svg class="title-block" width="800" height="780" viewBox="0 0 800 780" aria-label="Roots &amp; Resilience">
      <text class="title-word" x="60" y="663" font-size="138" fill="#ffffff" textLength="420" lengthAdjust="spacingAndGlyphs">ROOTS</text>
      <text class="title-word" x="490" y="663" font-size="158" fill="#555555" textLength="117" lengthAdjust="spacingAndGlyphs">&amp;</text>
      <text class="title-word" x="60" y="757" font-size="103" fill="#c40000" textLength="548" lengthAdjust="spacingAndGlyphs">RESILIENCE</text>
    </svg>

    <p class="subtitle-band">A Celebration of Culture,<br>Struggle and Achievement</p>

    <p class="tagline">The <em>History, Resistance</em> and <em>Excellence</em><br>of Black People in Africa and the Diaspora</p>

    <p class="author">SOLOMON RIDLEY</p>
  </main>
</body>
</html>
```